Office Wall Poster plus other Wall Decal quotes in office

We have redesigned our office & require parts of our Culture statement to be displayed in our office. Our company is KOVA Estate Agents Group and our brand is all about being KOVA .. integrity, honesty, authenticity etc.
We have two areas we wish to decorate.
1. Reception
2. Meeting Room

RECEPTION
We want our leading culture statement to be displayed as large A0 size in a framed POSTER PRINT in our reception. The frame will be black.
WORDING: 'There's a reason we're called KOVA. KOVA is the essence of who we are'
Our brand colors are red, white, black. Our Red is CMYK 12,99, 92,02
When we type our name KOVA, we always use Venera font (always in caps). I have attached a file I personally created with 3 different ideas (I am not a designer) but we are not happy with any of them but it will give you an idea of what we are looking for. We want a simple statement so it stands out and not too busy.

MEETING ROOM
We have one black feature wall in this room and wish to dress this with a collection of quotes from our main Culture statement. We will have these printed as 'stick on wall decals' We have provided a collection of 8 quotes for you to design. Wording is to be in white colour with the key words to be METALLIC SILVER & in caps. We were planning to arrange them ad-hoc on the wall singularly, but if you have any creative ideas on how to display these, we are open to suggestions. Please provide your ideas on how best to arrange these on the black wall. Maybe even in a circle to represent our logo? But we truly do not have a clue - we are only real estate agents, not designers. That is why we would love suggetions on how best to make our Culture Statements work best.
Best of luck and we are excited to see your ideas!

Target Market(s)

Our clients need to get a great feel for what we are all about when they visit our office. Our culture needs to be seen and felt.

Industry/Entity Type

Real Estate

Font styles to use
Other font styles liked:
• We use Venera font when we type our name KOVA

Colors
EB3D1F
EC4F4E
F09395
F8D3D4
FCEDEE

Requirements
Should not have
• Not too busy, simple statements, easy to read

```html
<!DOCTYPE html>
<html lang="en">
<head>
<meta charset="utf-8">
<title>KOVA Estate Agents Group — Reception Poster</title>
<link rel="stylesheet" href="https://fonts.googleapis.com/css2?family=Jura:wght@300;400&family=Orbitron:wght@600;700;800&family=Playfair+Display:wght@900&display=swap">
<style>
  :root {
    --paper-light: #f7f3ee;
    --paper-warm: #ede6de;
    --brand-red: #c41e2e;
    --ink-grey: #8a8a8c;
    --ink-grey-dark: #7b7b7d;
    --name-tint: #e6ddd3;
  }
  html, body {
    margin: 0;
    padding: 0;
    width: 1000px;
    height: 1200px;
    overflow: hidden;
  }
  .poster {
    display: block;
    width: 1000px;
    height: 1200px;
    background: radial-gradient(ellipse at 70% 20%, var(--paper-light) 0%, var(--paper-warm) 100%);
  }
  .company-name {
    font-family: "Orbitron", sans-serif;
    font-weight: 700;
    font-size: 40px;
    fill: var(--name-tint);
  }
  .quote-mark {
    font-family: "Playfair Display", serif;
    font-weight: 900;
    font-size: 210px;
    fill: var(--brand-red);
  }
  .line-light {
    font-family: "Jura", sans-serif;
    font-weight: 300;
    fill: var(--ink-grey);
  }
  .line-reason { font-size: 44px; }
  .line-called { font-size: 60px; }
  .line-is-the { font-size: 74px; }
  .line-name {
    font-family: "Orbitron", sans-serif;
    font-weight: 800;
    font-size: 112px;
    fill: var(--brand-red);
  }
  .line-essence {
    font-family: "Orbitron", sans-serif;
    font-weight: 700;
    font-size: 54px;
    fill: var(--ink-grey-dark);
  }
  .line-who {
    font-family: "Orbitron", sans-serif;
    font-weight: 600;
    font-size: 44px;
    fill: var(--brand-red);
  }
</style>
</head>
<body>
<svg class="poster" viewBox="0 0 1000 1200" xmlns="http://www.w3.org/2000/svg">
  <text class="company-name" x="500" y="420" text-anchor="middle" textLength="620" lengthAdjust="spacingAndGlyphs">KOVA Estate Agents Group</text>

  <g class="culture-quote">
    <text class="quote-mark" x="82" y="838">“</text>
    <text class="line-light line-reason" x="200" y="742" textLength="500" lengthAdjust="spacingAndGlyphs">There's a reason</text>
    <text class="line-light line-called" x="198" y="798" textLength="502" lengthAdjust="spacingAndGlyphs">we're called</text>
    <text class="line-name" x="196" y="898" textLength="602" lengthAdjust="spacingAndGlyphs">KOVA</text>
    <text class="line-light line-is-the" x="196" y="962" textLength="606" lengthAdjust="spacingAndGlyphs">KOVA is the</text>
    <text class="line-essence" x="198" y="1023" textLength="604" lengthAdjust="spacingAndGlyphs">essence of</text>
    <text class="line-who" x="200" y="1080" textLength="600" lengthAdjust="spacingAndGlyphs">WHO WE ARE</text>
    <text class="quote-mark" x="814" y="1210">”</text>
  </g>
</svg>
</body>
</html>
```